Civic Counsel and Advocacy Network needs poster design for landlord/tenant cases

We're seeking a poster design (11x17) to spread awareness for services by "Civic Counsel and Advocacy Network". The services they're trying to communicate are regarding housing/landlord/tenant matters.

We'd like the poster to (1) reflect the color scheme and branding of their website www.ccanplumridge.org, (2) contain the following copy: "Everyone needs safe and suitable housing, whether they own a home or rent one. When homelessness threatens, we at CCN help clients free of charge through eviction diversion programs and mortgage/tax foreclosure prevention.", and (3) contain their contact information:

Civic Counsel and Advocacy Network, Inc.
"We are YOUR Law Firm for Housing matters"
Contact us at: (555) 314-6082
housing @ccanplumridge.org
www.ccanplumridge.org

Target Market(s)

People who may be facing eviction or homelessness

Industry/Entity Type

Legal

Colors
0054AA
0677BA
7BADD7
CADEEF
E8F1F8
FFC000
F8CF3A
FAE287
FDF2CF
FEFAEE
EB3D1F
EC4F4E
F09395
F8D3D4
FCEDEE

Requirements
Must have
• Must include colors from website: https://ccanplumridge.org/

```html
<!DOCTYPE html>
<html lang="en">
<head>
<meta charset="utf-8">
<title>Civic Counsel and Advocacy Network – Housing Poster</title>
<link rel="stylesheet" href="https://fonts.googleapis.com/css2?family=Libre+Baskerville:wght@400;700&family=Source+Sans+3:wght@400;600&display=swap">
<style>
  :root {
    --navy: #1d2a78;
    --navy-deep: #17206a;
    --navy-light: #3d5ba6;
    --red: #e04a33;
    --white: #ffffff;
    --ink-blue: #27348b;
    --grey-text: #5b5f6a;
    --photo-warm: #cdb8a4;
    --photo-cool: #9aa6b8;
  }
  * { margin: 0; padding: 0; box-sizing: border-box; }
  html, body { width: 934px; height: 1200px; overflow: hidden; background: var(--white); }
  .poster {
    position: relative; width: 934px; height: 1200px; overflow: hidden;
    background: linear-gradient(180deg, var(--navy-light) 0%, var(--navy) 45%, var(--navy-deep) 100%);
    font-family: "Source Sans 3", "Myriad Pro", Arial, sans-serif;
  }
  .header-band {
    position: absolute; left: 0; top: 0; width: 343px; height: 166px;
    background: linear-gradient(135deg, var(--navy-deep) 0%, var(--navy) 50%, var(--navy-light) 100%);
  }
  .brand {
    position: absolute; left: 343px; top: 0; right: 0; height: 166px; background: var(--white);
    display: flex; align-items: center; padding-left: 38px; gap: 14px;
  }
  .brand-dot {
    width: 100px; height: 100px; border-radius: 50%; background: var(--navy); flex: none;
    box-shadow: 0 0 0 4px var(--white), 0 0 0 6px var(--navy);
  }
  .brand-name {
    font-family: "Libre Baskerville", Georgia, serif; font-weight: 700; font-size: 17px;
    color: var(--grey-text); line-height: 1.35; letter-spacing: 0.3px;
    border-bottom: 2px solid var(--ink-blue); padding-bottom: 6px;
  }
  .hero-photo {
    position: absolute; left: 0; top: 166px; width: 934px; height: 506px;
    background: linear-gradient(160deg, #e9e3dc 0%, var(--photo-warm) 45%, #8d7a6a 75%, var(--photo-cool) 100%);
  }
  .info-panel {
    position: absolute; left: 343px; top: 672px; right: 0; height: 392px;
    background: var(--white); border-bottom-left-radius: 72px;
  }
  .inset-photo {
    position: absolute; border-radius: 50%; border: 5px solid var(--navy); background-clip: padding-box;
  }
  .inset-keys { left: 452px; top: 522px; width: 220px; height: 220px;
    background: radial-gradient(circle at 55% 45%, #c98b6e 0%, #d9c2b4 45%, #eef0f3 100%); }
  .inset-family { left: 654px; top: 495px; width: 252px; height: 252px;
    background: radial-gradient(circle at 50% 60%, #9fb6d6 0%, #d8dde6 50%, #f4f4f4 100%); }

  .headline {
    position: absolute; left: 42px; top: 735px; width: 300px;
    font-family: "Libre Baskerville", Georgia, serif; font-weight: 700; font-size: 32px;
    line-height: 39px; color: var(--white); text-transform: uppercase; letter-spacing: -0.5px;
  }
  .headline .accent { color: var(--red); }
  .org-name {
    position: absolute; left: 44px; top: 920px; width: 290px;
    color: var(--white); font-size: 21px; line-height: 27px; font-weight: 600;
  }
  .cta {
    position: absolute; left: 44px; top: 1030px; width: 264px; height: 36px;
    border: 2px solid var(--white); border-radius: 18px; background: var(--red);
    color: var(--white); font-size: 21px; font-weight: 600; line-height: 32px; text-align: center;
  }
  .lead {
    position: absolute; left: 392px; top: 745px; width: 500px;
    color: var(--red); font-size: 28px; line-height: 34px; font-weight: 400;
  }
  .divider { position: absolute; left: 396px; top: 868px; width: 206px; height: 4px; background: var(--red); }
  .body-copy {
    position: absolute; left: 396px; top: 900px; width: 490px;
    color: var(--ink-blue); font-size: 21px; line-height: 26.5px; text-align: justify;
  }
  .contact-bar {
    position: absolute; left: 0; top: 1125px; width: 934px; height: 40px;
    display: flex; align-items: center; color: var(--white); font-size: 22px; font-weight: 600;
  }
  .contact-item { position: absolute; display: flex; align-items: center; gap: 9px; white-space: nowrap; }
  .contact-item svg { width: 22px; height: 22px; flex: none; }
  .contact-email { left: 42px; }
  .contact-phone { left: 404px; }
  .contact-web { left: 641px; }
  .base-stripe { position: absolute; left: 0; bottom: 0; width: 934px; height: 17px; background: var(--red); }
</style>
</head>
<body>
<main class="poster">
  <div class="header-band"></div>
  <header class="brand">
    <span class="brand-dot"></span>
    <div class="brand-name">CIVIC COUNSEL AND ADVOCACY<br>NETWORK INCORPORATED</div>
  </header>

  <div class="hero-photo" role="img" aria-label="Photo of a worried couple on a sofa reviewing bills with a calculator and coffee cup"></div>
  <div class="info-panel"></div>
  <div class="inset-photo inset-keys" role="img" aria-label="Photo of hands holding house keys and a small model house"></div>
  <div class="inset-photo inset-family" role="img" aria-label="Photo of a smiling family sitting under a roof shape"></div>

  <h1 class="headline">We are your<br><span class="accent">Law firm</span><br>for housing<br>matters</h1>
  <p class="org-name">Civic Counsel and Advocacy Network, Inc.</p>
  <a class="cta" href="https://ccanplumridge.org/" style="text-decoration:none">CONTACT US NOW</a>

  <p class="lead">Everyone needs safe and suitable housing, whether they own a home or rent one.</p>
  <div class="divider"></div>
  <p class="body-copy">When homelessness threatens, we at CCN help clients free of charge through eviction diversion programs and mortgage/tax foreclosure prevention.</p>

  <footer class="contact-bar">
    <div class="contact-item contact-email">
      <svg viewBox="0 0 22 22"><circle cx="11" cy="11" r="9.5" fill="none" stroke="#e04a33" stroke-width="2"/><rect x="6" y="7.5" width="10" height="7" fill="#e04a33"/><path d="M6 7.5 L11 11.5 L16 7.5" fill="none" stroke="#1d2a78" stroke-width="1.2"/></svg>
      <span>housing @ccanplumridge.org</span>
    </div>
    <div class="contact-item contact-phone">
      <svg viewBox="0 0 22 22"><circle cx="11" cy="11" r="9.5" fill="none" stroke="#e04a33" stroke-width="2"/><path d="M7.5 6.5 C7 9.5 10 14.5 14.5 15 L15.5 13.5 L13.5 12 L12.5 13 C11 12.3 9.8 11 9.2 9.5 L10.2 8.5 L8.8 6 Z" fill="#e04a33"/></svg>
      <span>(555) 314-6082</span>
    </div>
    <div class="contact-item contact-web">
      <svg viewBox="0 0 22 22" fill="none" stroke="#e04a33" stroke-width="1.6"><circle cx="11" cy="11" r="9.5" stroke-width="2"/><circle cx="11" cy="11" r="5.5"/><ellipse cx="11" cy="11" rx="2.3" ry="5.5"/><path d="M5.5 11 H16.5"/></svg>
      <span>www.ccanplumridge.org</span>
    </div>
  </footer>
  <div class="base-stripe"></div>
</main>
</body>
</html>
```